Motorcycle Shop Business Card

New business card for Motorcycle repair and customization shop.Business name: Copper Falcon Chris Morris443-865-5190, 7214 Quarry Lane Brayford, MD 21099. www.dale@copperfalconcustoms.example. I uploaded some motorcycle images and logo and a couple of our calendar shoots. They do not have to be used on card just examples of some of our work and past graphic work.
We work on Vantor Brennick and Custom Built Motorcycles.

Looking for front and back design

Target Market(s)

Motorcycle owners

Industry/Entity Type

Motorcycle Part

```html
<!DOCTYPE html>
<html lang="en">
<head>
<meta charset="utf-8">
<title>Copper Falcon Customs – Business Card</title>
<link rel="stylesheet" href="https://fonts.googleapis.com/css2?family=Roboto:wght@400;700&display=swap">
<style>
  :root {
    --stage: #b9b9b9;
    --ink: #111111;
    --paper: #ffffff;
    --muted: #6f6f6f;
    --band: #0d0d0d;
  }
  * { box-sizing: border-box; margin: 0; padding: 0; }
  html, body { width: 1200px; height: 885px; overflow: hidden; }
  body {
    background: var(--stage);
    font-family: "Roboto", Arial, sans-serif;
    position: relative;
  }
  .card {
    position: absolute;
    width: 520px;
    height: 297px;
    border-radius: 2px;
    overflow: hidden;
  }
  .card-back {
    left: 80px;
    top: 130px;
    background: var(--ink);
    color: var(--paper);
  }
  .card-front {
    left: 600px;
    top: 450px;
    background: var(--paper);
    color: var(--ink);
  }
  .brand-name {
    position: absolute;
    left: 0;
    right: 0;
    text-align: center;
    font-weight: 700;
    font-size: 40px;
    letter-spacing: 1px;
  }
  .card-back .brand-name { top: 92px; color: var(--paper); }
  .card-front .brand-name { top: 46px; color: var(--ink); }
  .back-web {
    position: absolute;
    left: 0;
    right: 0;
    bottom: 48px;
    text-align: center;
    font-size: 13px;
    letter-spacing: 3px;
  }
  .name-band {
    position: absolute;
    left: 0;
    right: 0;
    top: 146px;
    height: 34px;
    background: var(--band);
  }
  .holder-name {
    position: absolute;
    left: 150px;
    top: 146px;
    height: 34px;
    line-height: 34px;
    padding: 0 18px;
    color: var(--paper);
    font-weight: 700;
    font-size: 19px;
    text-transform: uppercase;
  }
  .address {
    position: absolute;
    right: 26px;
    top: 100px;
    text-align: right;
    font-style: normal;
    font-size: 13px;
    line-height: 18px;
    color: var(--muted);
  }
  .contact-list {
    position: absolute;
    left: 36px;
    bottom: 34px;
    list-style: none;
    font-size: 14px;
    color: var(--muted);
  }
  .contact-list li {
    display: flex;
    align-items: center;
    gap: 8px;
    line-height: 24px;
  }
  .contact-list svg { width: 12px; height: 12px; fill: var(--ink); }
</style>
</head>
<body>

  <section class="card card-back" aria-label="Business card back">
    <div class="brand-name">Copper Falcon</div>
    <div class="back-web">www.dale@copperfalconcustoms.example</div>
  </section>

  <section class="card card-front" aria-label="Business card front">
    <div class="brand-name">Copper Falcon</div>
    <div class="name-band"></div>
    <div class="holder-name">Dale Fenwick</div>
    <address class="address">7214 Quarry Lane<br>Brayford, MD 21099.</address>
    <ul class="contact-list">
      <li>
        <svg viewBox="0 0 24 24" aria-hidden="true"><path d="M6.6 10.8a15.1 15.1 0 0 0 6.6 6.6l2.2-2.2c.3-.3.7-.4 1-.2 1.1.4 2.3.6 3.6.6.6 0 1 .4 1 1V20c0 .6-.4 1-1 1A17 17 0 0 1 3 4c0-.6.4-1 1-1h3.5c.6 0 1 .4 1 1 0 1.3.2 2.5.6 3.6.1.3 0 .7-.2 1z"/></svg>
        410-555-0137
      </li>
      <li>
        <svg viewBox="0 0 24 24" aria-hidden="true"><circle cx="12" cy="12" r="10"/></svg>
        www.dale@copperfalconcustoms.example
      </li>
    </ul>
  </section>

</body>
</html>
```